Consumer facing site as a spin off of primary B2B site

Create a consumer-focused website for a product that transforms TVs into digital frames, based on primary digital signage website https://lumora-view.com.
Requirements
1. Homepage
• Hero Section: Engaging imagery of the product in use in home settings, with a clear, concise value proposition.
• Introduction Video: A short, engaging video that explains the product's key features and benefits.
• Clear Product Value Proposition: "Transform your TVs into shared family albums", "Easily connect with loved ones through photos and videos", etc.
• How It Works: A simple step-by-step guide or infographic showing how easy it is to set up and use.
• Testimonials: Snippets from real users showcasing how the product has enhanced their home and family life.
• Visual appeal: Images of the product in use (families enjoying content, simple setup on TVs)
• Clear Calls to Action: "Try for Free," "Learn More"
2. Product Details Page
• Features Overview: Detailed descriptions of key features, including screen size flexibility, connectivity, social features, and interactivity.
• Simplify Feature Language: Avoid technical jargon, focus on benefits for families (easy sharing, remote management, slideshow options)
• Showcase Scenarios: "Share baby photos with grandparents", "Keep in touch while traveling", "Send video messages for birthdays"
• Technical Specifications: Information on app compatibility, resolution support, storage options, and any hardware requirements.
• Gallery: High-resolution images showing the product's interface, app screenshots, and examples of it being used in various home environments.
3. FAQ & Support
• Frequently Asked Questions: Answers to common queries about setup, compatibility, subscriptions, and troubleshooting.
• Setup Guides and Tutorials: Step-by-step instructions and video tutorials for setting up and personalizing the product.
• Customer Support: Contact form, live chat, and support hotline information for users needing assistance.
4. Pricing & Subscription Plans
• Details on pricing for the app/service, with a comparison chart if multiple tiers are offered.
• Subscription Benefits: A breakdown of what's included in the subscription, such as cloud storage, exclusive features, and any family sharing options.
• Free Trial Offer: Information on how to start a free trial, what it includes, and how users can subscribe afterward.
5. About Us
• Our Story: Background on LumoraView, the team, and the mission behind the product.
• Vision for Families: Explanation of how the product aims to bring families closer together.
• Sustainability and Social Responsibility
Also need a quick UI refresh (Style/Icons) for the companion mobile app. See attached document

```html
<!DOCTYPE html>
<html lang="en">
<head>
<meta charset="utf-8">
<title>LumoraView – Turn Your TVs Into Shared Family Albums</title>
<link href="https://fonts.googleapis.com/css2?family=Montserrat:wght@400;500;600;700&family=Nunito:wght@700;800&display=swap" rel="stylesheet">
<style>
:root{
  --purple:#6d45a6;
  --purple-soft:#8a63b9;
  --lavender:#ece8f4;
  --lavender-deep:#c9b8e0;
  --ink:#2b2b2b;
  --white:#ffffff;
  --black:#000000;
  --teal:#2d6270;
  --teal-dark:#173c47;
}
*{box-sizing:border-box;margin:0;padding:0}
html,body{width:1200px;height:3495px;overflow:hidden}
body{font-family:"Montserrat",sans-serif;color:var(--ink);background:var(--white)}
.page{position:relative;width:1200px;height:3495px;overflow:hidden;background:var(--white)}
.abs{position:absolute}
.upper{text-transform:uppercase}

/* Header */
.topbar{position:absolute;left:0;top:0;width:1200px;height:44px}
.topbar-item{position:absolute;top:0;height:44px;display:flex;align-items:center;gap:12px;color:var(--white);font-size:13px;font-weight:500;letter-spacing:.3px}
.try-btn{position:absolute;left:988px;top:6px;width:160px;height:32px;border:1px solid var(--white);color:var(--white);font-size:13px;font-weight:600;display:flex;align-items:center;justify-content:center;gap:10px}
.brand{position:absolute;left:111px;top:38px;font-weight:700;font-size:42px;color:var(--purple);letter-spacing:-.5px;display:flex;align-items:center;gap:14px}
.brand-dot{width:26px;height:26px;border-radius:50%;background:var(--purple)}
.main-nav{position:absolute;top:74px;left:537px;display:flex;gap:46px;font-size:15px;font-weight:500;text-transform:uppercase;letter-spacing:.3px}
.main-nav a{color:var(--ink);text-decoration:none}
.main-nav a.active{color:var(--purple)}

/* Hero */
.hero-art{position:absolute;left:0;top:120px}
.hero-title{position:absolute;left:0;top:348px;width:1200px;text-align:center;color:var(--white);font-size:46px;font-weight:600;line-height:72px;letter-spacing:1px;text-transform:uppercase}
.cta{position:absolute;display:flex;align-items:center;justify-content:space-between;background:var(--purple);color:var(--white);font-weight:600;font-size:25px;letter-spacing:.5px;text-transform:uppercase;border:3px solid var(--white);padding:0 8px 0 20px}
.cta-square{width:52px;height:52px;background:var(--white)}
.hero-cta{left:460px;top:532px;width:280px;height:66px}

/* How it works */
.section-title{position:absolute;left:0;width:1200px;text-align:center;color:var(--purple);font-weight:500;font-size:32px;letter-spacing:.8px;text-transform:uppercase}
.step-label{position:absolute;text-align:center;font-size:18px;font-weight:500;line-height:36px;color:var(--ink);text-transform:uppercase;letter-spacing:.3px}

/* Video */
.video{position:absolute;left:208px;top:1574px;width:783px;height:424px;border-radius:90px 0 0 0;overflow:hidden;background:linear-gradient(180deg,var(--teal) 0%,var(--teal-dark) 100%)}
.video-shadow{position:absolute;left:216px;top:1584px;width:783px;height:424px;border-radius:90px 0 40px 0;background:var(--lavender-deep)}
.video-frame{position:absolute;left:30px;top:34px;width:725px;height:360px;background:linear-gradient(160deg,#4e7c86 0%,#3b6570 55%,#29505b 100%);opacity:.9}
.video-name{position:absolute;left:0;top:150px;width:783px;text-align:center;font-family:"Nunito",sans-serif;font-weight:800;font-size:50px;color:var(--white)}
.video-tag{position:absolute;left:0;top:232px;width:783px;text-align:center;font-family:"Nunito",sans-serif;font-weight:700;font-size:23px;color:var(--white)}
.video-controls{position:absolute;left:0;bottom:0;width:783px;height:70px;background:linear-gradient(180deg,rgba(0,0,0,0),rgba(0,0,0,.55))}
.video-time{position:absolute;left:50px;top:20px;color:var(--white);font-size:17px;font-family:Arial,sans-serif}
.video-track{position:absolute;left:12px;bottom:12px;width:755px;height:4px;background:rgba(255,255,255,.35)}
.video-track span{display:block;width:54%;height:4px;background:rgba(255,255,255,.85)}

/* Testimonials */
.avatar{position:absolute;border-radius:50%;background:radial-gradient(circle at 50% 40%,#d9c9bd 0%,#9c8a82 60%,#5b5f6b 100%)}
.avatar-main{position:absolute;left:555px;top:2171px;width:100px;height:100px;border-radius:50%;border:2px solid var(--purple);padding:6px;background:var(--white)}
.avatar-main span{display:block;width:100%;height:100%;border-radius:50%;background:radial-gradient(circle at 50% 40%,#e0cdbf 0%,#6e87a6 65%,#3d5877 100%)}
.quote-mark{position:absolute;left:478px;top:2130px;font-family:Georgia,serif;font-size:200px;line-height:1;color:#ededed}
.quote-text{position:absolute;left:250px;top:2296px;width:700px;text-align:center;font-size:17px;line-height:34.3px;color:var(--ink)}
.quote-name{position:absolute;left:0;top:2454px;width:1200px;text-align:center;font-size:21px;color:var(--purple);letter-spacing:.8px;text-transform:uppercase}

/* Pricing */
.pricing-title{position:absolute;left:110px;top:2592px;width:490px;color:var(--purple);font-weight:500;font-size:30px;line-height:58.5px;letter-spacing:.8px;text-transform:uppercase}
.pricing-copy{position:absolute;left:111px;top:2776px;width:470px;font-size:17px;line-height:34.5px;color:var(--ink)}
.pricing-cta{left:111px;top:2918px;width:282px;height:68px;border:none;padding:0 8px 0 30px}
.pricing-backdrop{position:absolute;left:832px;top:2779px;width:254px;height:244px;background:var(--purple-soft);border-radius:0 28px 0 40px}
.pricing-photo{position:absolute;left:616px;top:2577px;width:442px;height:411px;background:linear-gradient(180deg,#eef0f4 0%,#d7dce6 55%,#c59a63 78%,#a8733c 100%)}

/* Footer */
.footer-art{position:absolute;left:0;top:3030px}
.footer-brand{position:absolute;left:0;top:3224px;width:1200px;display:flex;justify-content:center;align-items:center;gap:16px;font-weight:700;font-size:44px;color:var(--white)}
.footer-brand .brand-dot{background:var(--white)}
.footer-nav{position:absolute;left:0;top:3338px;width:1200px;display:flex;justify-content:center;gap:46px;font-size:16px;font-weight:600;text-transform:uppercase}
.footer-nav a{color:var(--white);text-decoration:none}
.copyright{position:absolute;left:0;top:3407px;width:1200px;text-align:center;color:var(--white);font-size:16px;font-weight:600;text-transform:uppercase}
</style>
</head>
<body>
<div class="page">

  <!-- Header -->
  <header>
    <svg class="topbar" width="1200" height="44" viewBox="0 0 1200 44">
      <polygon points="455,0 1200,0 1200,44 480,44" fill="var(--purple)"/>
    </svg>
    <div class="topbar-item" style="left:523px">
      <svg width="14" height="14" viewBox="0 0 24 24"><path d="M6.6 10.8a15 15 0 0 0 6.6 6.6l2.2-2.2a1 1 0 0 1 1-.25 11.4 11.4 0 0 0 3.6.57 1 1 0 0 1 1 1V20a1 1 0 0 1-1 1A17 17 0 0 1 3 4a1 1 0 0 1 1-1h3.5a1 1 0 0 1 1 1c0 1.25.2 2.45.57 3.6a1 1 0 0 1-.25 1z" fill="#fff"/></svg>
      <span>(555) 014-2290</span>
    </div>
    <div class="topbar-item" style="left:722px">
      <svg width="15" height="11" viewBox="0 0 15 11"><rect x="0.5" y="0.5" width="14" height="10" fill="#fff"/><path d="M0.5 0.5 L7.5 6 L14.5 0.5" stroke="var(--purple)" fill="none"/></svg>
      <span>INFO@LUMORA-VIEW.COM</span>
    </div>
    <div class="try-btn">TRY FOR FREE
      <svg width="18" height="10" viewBox="0 0 18 10"><path d="M0 5h16M12 1l4 4-4 4" stroke="#fff" fill="none" stroke-width="1.3"/></svg>
    </div>
    <div class="brand"><span class="brand-dot"></span>LumoraView</div>
    <nav class="main-nav">
      <a class="active" href="#">Home</a>
      <a href="#">How It Works</a>
      <a href="#">Testimonials</a>
      <a href="#">Contact Us</a>
    </nav>
  </header>

  <!-- Hero -->
  <section class="hero">
    <svg class="hero-art" width="1200" height="1218" viewBox="0 120 1200 1218">
      <rect x="0" y="120" width="1200" height="1218" fill="var(--lavender)"/>
      <polygon points="0,540 0,600 600,889 1065,615 600,845" fill="var(--purple)"/>
      <polygon points="0,120 1200,120 1200,548 600,845 0,555" fill="var(--white)"/>
      <defs>
        <linearGradient id="heroPhoto" x1="0" y1="0" x2="1" y2="1">
          <stop offset="0" stop-color="#3a3f4d"/>
          <stop offset="0.5" stop-color="#5a5b63"/>
          <stop offset="1" stop-color="#2b2d35"/>
        </linearGradient>
      </defs>
      <polygon role="img" aria-label="Couple relaxing on a sofa watching a streaming show on their living room TV" points="0,120 1200,120 1200,535 600,830 0,538" fill="url(#heroPhoto)"/>
    </svg>
    <h1 class="hero-title">Transform your TVs into shared<br>family albums</h1>
    <a class="cta hero-cta">Learn More <span class="cta-square"></span></a>
  </section>

  <!-- How it works -->
  <section class="how-it-works">
    <h2 class="section-title" style="top:948px">How It Works</h2>
    <svg class="abs" style="left:0;top:960px" width="1200" height="240" viewBox="0 960 1200 240">
      <g fill="none" stroke="var(--purple)" stroke-width="1.5" stroke-dasharray="6 5">
        <circle cx="301" cy="1061" r="88"/>
        <circle cx="598" cy="1121" r="88"/>
        <circle cx="898" cy="1061" r="88"/>
        <path d="M386 1080 C420 1115,470 1120,512 1116"/>
        <path d="M684 1118 C740 1128,790 1110,820 1085"/>
      </g>
      <path d="M505 1108 l10 8 -10 8" fill="none" stroke="var(--purple)" stroke-width="2"/>
      <path d="M812 1088 l12 -6 -2 13" fill="none" stroke="var(--purple)" stroke-width="2"/>
      <g fill="var(--purple)">
        <circle cx="301" cy="1061" r="80"/>
        <circle cx="598" cy="1121" r="80"/>
        <circle cx="898" cy="1061" r="80"/>
      </g>
      <g fill="none" stroke="#fff" stroke-width="3" stroke-linejoin="round" stroke-linecap="round">
        <!-- computer -->
        <rect x="258" y="1013" width="88" height="62" rx="4"/>
        <path d="M285 1040 l10-10 M290 1048 l12-12"/>
        <path d="M290 1075 v10 h24 v-10"/>
        <path d="M266 1089 h72 l8 18 h-88 z"/>
        <path d="M276 1097 h52" stroke-dasharray="3 3"/>
        <!-- code window -->
        <rect x="553" y="1075" width="90" height="70" rx="4"/>
        <path d="M553 1090 h90"/>
        <path d="M565 1105 l-6 5 6 5 M575 1103 l-4 14 M581 1105 l6 5 -6 5"/>
        <path d="M595 1108 h36 M565 1125 h30 M600 1125 h30 M565 1134 h44"/>
        <path d="M588 1145 v8 h20 v-8"/>
        <!-- sign-in form -->
        <circle cx="862" cy="1027" r="12"/>
        <path d="M855 1034 a8 8 0 0 1 14 0"/>
        <rect x="888" y="1015" width="66" height="24" rx="6"/>
        <path d="M898 1027 h46"/>
        <circle cx="858" cy="1061" r="5"/>
        <path d="M863 1061 h14 M872 1061 v5"/>
        <rect x="888" y="1049" width="66" height="24" rx="6"/>
        <path d="M898 1061 h6 M913 1061 h6 M928 1061 h6 M943 1061 h4"/>
        <rect x="852" y="1084" width="102" height="26" rx="13"/>
        <path d="M894 1097 l6 5 10-10"/>
      </g>
    </svg>
    <p class="step-label" style="left:150px;top:1167px;width:304px">On your phone or<br>computer</p>
    <p class="step-label" style="left:440px;top:1236px;width:316px">Enter the code</p>
    <p class="step-label" style="left:740px;top:1167px;width:316px">Sign in to your LumoraView<br>account</p>
  </section>

  <!-- Intro video -->
  <section class="intro-video">
    <h2 class="section-title" style="top:1420px;line-height:63px">Easily connect with loved ones through<br>photos and videos</h2>
    <div class="video-shadow"></div>
    <div class="video" role="img" aria-label="Introduction video showing photos displayed across several TV screens in a modern office">
      <div class="video-frame"></div>
      <div class="video-name">LumoraView</div>
      <div class="video-tag">Displaying Content Across Multiple Screens, Effortlessly.</div>
      <div class="video-controls">
        <svg class="abs" style="left:16px;top:22px" width="14" height="16" viewBox="0 0 14 16"><path d="M1 1 L13 8 L1 15 Z" fill="#fff"/></svg>
        <span class="video-time">0:00 / 0:58</span>
        <svg class="abs" style="left:634px;top:20px" width="22" height="20" viewBox="0 0 22 20"><path d="M2 7h4l5-5v16l-5-5H2z" fill="#fff"/><path d="M14 6a5 5 0 0 1 0 8M16 3a9 9 0 0 1 0 14" stroke="#fff" fill="none" stroke-width="1.8"/></svg>
        <svg class="abs" style="left:696px;top:22px" width="16" height="16" viewBox="0 0 16 16"><path d="M1 5V1h4M11 1h4v4M15 11v4h-4M5 15H1v-4" stroke="#fff" fill="none" stroke-width="2"/></svg>
        <svg class="abs" style="left:760px;top:21px" width="4" height="18" viewBox="0 0 4 18"><circle cx="2" cy="2" r="2" fill="#fff"/><circle cx="2" cy="9" r="2" fill="#fff"/><circle cx="2" cy="16" r="2" fill="#fff"/></svg>
        <div class="video-track"><span></span></div>
      </div>
    </div>
  </section>

  <!-- Testimonials -->
  <section class="testimonials">
    <h2 class="section-title" style="top:2086px">Testimonials</h2>
    <div class="avatar" role="img" aria-label="Customer portrait" style="left:301px;top:2144px;width:42px;height:42px"></div>
    <div class="avatar" role="img" aria-label="Customer portrait" style="left:103px;top:2215px;width:38px;height:38px"></div>
    <div class="avatar" role="img" aria-label="Customer portrait" style="left:870px;top:2199px;width:52px;height:52px"></div>
    <div class="avatar" role="img" aria-label="Customer portrait" style="left:1117px;top:2154px;width:68px;height:68px"></div>
    <div class="avatar" role="img" aria-label="Customer portrait" style="left:210px;top:2315px;width:68px;height:68px"></div>
    <div class="avatar" role="img" aria-label="Customer portrait" style="left:15px;top:2396px;width:98px;height:98px"></div>
    <div class="avatar" role="img" aria-label="Customer portrait" style="left:937px;top:2419px;width:52px;height:52px"></div>
    <div class="avatar" role="img" aria-label="Customer portrait" style="left:1099px;top:2452px;width:66px;height:66px"></div>
    <div class="quote-mark">“</div>
    <div class="avatar-main" role="img" aria-label="Portrait of the featured customer"><span></span></div>
    <p class="quote-text">Sed ut perspiciatis unde omnis iste natus error sit voluptatem accusantium doloremque laudantium, totam rem aperiam, eaque ipsa quae ab illo inventore veritatis et quasi architecto beatae vitae dicta sunt explicabo. Nemo enim ipsam voluptatem quia voluptas sit.</p>
    <p class="quote-name">- Lorem Ipsum</p>
  </section>

  <!-- Pricing -->
  <section class="pricing">
    <h2 class="pricing-title">Simplify your digital signage with transparent pricing</h2>
    <p class="pricing-copy">Embrace the simplicity and affordability of LumoraView’s pricing designed for every budget. With our flat-rate plan, you unlock unlimited potential to display content</p>
    <a class="cta pricing-cta">Read More <span class="cta-square"></span></a>
    <div class="pricing-backdrop"></div>
    <div class="pricing-photo" role="img" aria-label="Hand reaching toward wooden blocks printed with percent signs"></div>
  </section>

  <!-- Footer -->
  <footer>
    <svg class="footer-art" width="1200" height="465" viewBox="0 3030 1200 465">
      <polygon points="598,3046 120,3322 598,3091 1200,3392 1200,3331" fill="var(--purple-soft)"/>
      <polygon points="598,3091 0,3410 0,3495 1200,3495 1200,3392" fill="var(--black)"/>
    </svg>
    <div class="footer-brand"><span class="brand-dot"></span>LumoraView</div>
    <nav class="footer-nav">
      <a href="#">Home</a>
      <a href="#">How It Works</a>
      <a href="#">Testimonials</a>
      <a href="#">Contact Us</a>
    </nav>
    <p class="copyright">Copyright © 2024 LumoraView</p>
  </footer>

</div>
</body>
</html>
```